Business Card Design Project

Recently had a new logo made up for my company and new business cards done as well. I have attached the logos for your viewing. Additional projects may be needed. Good luck!

Industry/Entity Type

Business

```html
<!DOCTYPE html>
<html lang="en">
<head>
<meta charset="utf-8">
<title>Halden Financial Group – Business Card Options</title>
<link rel="stylesheet" href="https://fonts.googleapis.com/css2?family=Jost:wght@400;500;600&family=Cinzel:wght@400&display=swap">
<style>
  :root {
    --backdrop: #7b4b2d;
    --card-black: #050505;
    --gold: #c8b58a;
    --gold-band: #cbb98d;
    --gold-card: #cfbd8f;
    --white: #ffffff;
    --faint-frame: #3a3428;
    --ink: #111111;
  }
  * { margin: 0; padding: 0; box-sizing: border-box; }
  html, body { width: 1200px; height: 821px; overflow: hidden; }
  body {
    position: relative;
    background: var(--backdrop);
    font-family: "Jost", sans-serif;
    color: var(--white);
  }
  .option-label {
    position: absolute;
    font-size: 31px;
    font-weight: 400;
    color: var(--white);
    text-align: center;
    width: 300px;
  }
  .card {
    position: absolute;
    width: 525px;
    height: 300px;
    background: var(--card-black);
    overflow: hidden;
  }
  .card--gold { background: var(--gold-card); }

  /* Front card */
  .brand-block {
    position: absolute;
    left: 82px; top: 55px;
    width: 100px;
    text-align: center;
  }
  .brand-square {
    display: block;
    width: 96px; height: 103px;
    margin: 0 auto;
    border: 7px solid var(--gold);
  }
  .brand-name {
    margin-top: 8px;
    font-size: 25px;
    font-weight: 500;
    letter-spacing: 1px;
    color: var(--gold);
    line-height: 1;
  }
  .brand-sub {
    margin-top: 5px;
    font-size: 10.5px;
    font-weight: 500;
    letter-spacing: 1.5px;
    color: var(--gold);
    white-space: nowrap;
    margin-left: -20px;
    margin-right: -20px;
  }
  .divider {
    position: absolute;
    left: 221px; top: 58px;
    width: 3px; height: 160px;
    background: linear-gradient(to bottom, rgba(255,255,255,0), rgba(255,255,255,0.85) 35%, rgba(255,255,255,0.85) 65%, rgba(255,255,255,0));
  }
  .contact {
    position: absolute;
    left: 246px; top: 57px;
  }
  .contact__name {
    font-size: 19px;
    font-weight: 600;
    letter-spacing: 0.8px;
    color: var(--gold);
    line-height: 1.1;
  }
  .contact__title {
    font-size: 12px;
    color: var(--white);
    margin-top: 2px;
  }
  .contact__list { list-style: none; margin-top: 12px; }
  .contact__item {
    display: flex;
    align-items: center;
    gap: 6px;
    font-size: 13.5px;
    line-height: 23px;
  }
  .contact__item svg { width: 10px; height: 10px; fill: var(--white); }
  .rule {
    position: absolute;
    left: 0; top: 266px;
    width: 100%; height: 2px;
    background: var(--white);
  }
  .address-band {
    position: absolute;
    left: 0; top: 271px;
    width: 100%; height: 29px;
    background: var(--gold-band);
    color: var(--ink);
    font-size: 12.5px;
    text-align: center;
    line-height: 29px;
  }

  /* Back cards */
  .web {
    position: absolute;
    left: 0; width: 100%;
    text-align: center;
    font-family: "Cinzel", serif;
    font-size: 15.5px;
    letter-spacing: 4px;
    color: var(--white);
  }
  .web__accent { color: var(--gold); }
  .faint-square {
    position: absolute;
    left: 158px; top: 38px;
    width: 208px; height: 220px;
    border: 10px solid var(--faint-frame);
  }
  .wordmark-wide {
    position: absolute;
    left: 0; width: 100%; top: 124px;
    text-align: center;
    font-size: 30px;
    font-weight: 500;
    letter-spacing: 3px;
    color: var(--gold);
  }
  .mark-square {
    position: absolute;
    display: flex;
    align-items: center;
    justify-content: center;
    font-size: 34px;
    font-weight: 500;
    letter-spacing: 3px;
  }
  .mark-square--white {
    left: 154px; top: 24px;
    width: 192px; height: 206px;
    border: 12px solid var(--white);
    color: var(--white);
  }
  .mark-square--gold {
    left: 153px; top: 25px;
    width: 193px; height: 205px;
    border: 10px solid var(--gold);
    color: var(--gold);
  }
</style>
</head>
<body>

  <div class="option-label" style="left:735px; top:18px;">Option # 1</div>
  <div class="option-label" style="left:132px; top:737px;">Option # 2</div>
  <div class="option-label" style="left:737px; top:737px;">Option # 3</div>

  <!-- Front -->
  <section class="card card--front" style="left:51px; top:73px;">
    <div class="brand-block">
      <span class="brand-square"></span>
      <div class="brand-name">HALDEN</div>
      <div class="brand-sub">FINANCIAL GROUP</div>
    </div>
    <div class="divider"></div>
    <div class="contact">
      <div class="contact__name">Grant M. Halden</div>
      <div class="contact__title">Estate Planning and Insurance Specialist</div>
      <ul class="contact__list">
        <li class="contact__item">
          <svg viewBox="0 0 10 10" aria-hidden="true"><path d="M2 0.5 L3.6 2.6 L2.7 3.6 C3.3 5 4.9 6.6 6.4 7.3 L7.4 6.4 L9.5 8 L8.5 9.5 C4.5 9.2 0.8 5.5 0.5 1.5 Z"/></svg>
          555-014-2739
        </li>
        <li class="contact__item">
          <svg viewBox="0 0 10 10" aria-hidden="true"><rect x="2.5" y="0.5" width="5" height="9" rx="1"/><rect x="3.4" y="1.6" width="3.2" height="5.6" fill="#050505"/></svg>
          555-014-6074
        </li>
        <li class="contact__item">
          <svg viewBox="0 0 10 10" aria-hidden="true"><rect x="0.5" y="2" width="9" height="6.5"/><path d="M0.8 2.3 L5 5.6 L9.2 2.3" stroke="#050505" stroke-width="0.9" fill="none"/></svg>
          ghalden@haldenfinancial.com
        </li>
        <li class="contact__item">
          <svg viewBox="0 0 10 10" aria-hidden="true"><circle cx="5" cy="5" r="4.5"/><path d="M0.5 5 H9.5 M5 0.5 V9.5 M5 0.5 C2.6 3 2.6 7 5 9.5 M5 0.5 C7.4 3 7.4 7 5 9.5" stroke="#050505" stroke-width="0.7" fill="none"/></svg>
          www.haldenfinancial.com
        </li>
      </ul>
    </div>
    <div class="rule"></div>
    <div class="address-band">4200 Orchard Parkway, Suite 310E, Brookvale, New York 11700</div>
  </section>

  <!-- Option 1 -->
  <section class="card card--back" style="left:621px; top:73px;">
    <div class="faint-square"></div>
    <div class="wordmark-wide">HALDEN FINANCIAL GROUP</div>
    <div class="web" style="top:266px;">WWW.<span class="web__accent">HALDEN</span>FINANCIAL.COM</div>
  </section>

  <!-- Option 2 -->
  <section class="card card--gold" style="left:51px; top:407px;">
    <div class="mark-square mark-square--white">HALDEN</div>
    <div class="web" style="top:262px;">WWW.HALDENFINANCIAL.COM</div>
  </section>

  <!-- Option 3 -->
  <section class="card card--back" style="left:618px; top:407px;">
    <div class="mark-square mark-square--gold">HALDEN</div>
    <div class="web" style="top:262px;">WWW.<span class="web__accent">HALDEN</span>FINANCIAL.COM</div>
  </section>

</body>
</html>
```